Navelock Insurance Solutions Drop Off Flyer

We need a clean, powerful, one page flyer to drop off at businesses. it needs to simple yet needs to jump out for a decision maker to read...

Target Market(s)

Business owners with over 50 employees.....all types of industries...

Industry/Entity Type

Insurance

Font styles to use
Serif
Sans Serif

Colors
0355a3
3176b5
85acd3
ffffff

Requirements
Must have
• You must include all wording on the PDF i included titled Navelock Flyer Idea. Of course, the color and layout is up to you but the wording needs to be included.
Nice to have
• Just a one page Letter size drop off

```html
<!DOCTYPE html>
<html lang="en">
<head>
<meta charset="utf-8">
<title>Navelock Insurance Solutions – Drop Off Flyer</title>
<link href="https://fonts.googleapis.com/css2?family=Montserrat:wght@400;700;800;900&family=Lato:wght@400;700;900&display=swap" rel="stylesheet">
<style>
  :root {
    --brand-blue: #0355a3;
    --mid-blue: #3176b5;
    --soft-blue: #85acd3;
    --navy: #0a2450;
    --orange: #f7941d;
    --orange-dark: #d97a0c;
    --white: #ffffff;
    --ink: #222222;
    --footer-grey: #4b4b4d;
    --divider: #b9b9b9;
  }
  * { margin: 0; padding: 0; box-sizing: border-box; }
  html, body { width: 896px; height: 1200px; overflow: hidden; background: var(--white); }
  body { font-family: "Lato", sans-serif; color: var(--ink); position: relative; }

  .masthead { position: absolute; top: 0; left: 0; width: 896px; height: 145px; display: flex; align-items: center; justify-content: center; gap: 16px; }
  .brand-mark { width: 56px; height: 56px; border-radius: 50%; background: var(--brand-blue); }
  .brand-name { font-family: "Montserrat", sans-serif; font-weight: 700; font-size: 30px; color: #1c1c1c; letter-spacing: 0.5px; }

  .hero { position: absolute; top: 145px; left: 0; width: 896px; height: 465px; background: var(--brand-blue); overflow: hidden; }
  .hero-photo { position: absolute; top: 0; right: 0; width: 440px; height: 465px;
    background: radial-gradient(circle at 55% 45%, #4aa3ff 0%, #1f5fae 22%, #0d2f66 55%, #071a3c 100%); }
  .hero-copy { position: absolute; left: 48px; top: 42px; }
  .headline { font-family: "Montserrat", sans-serif; font-weight: 900; font-size: 112px; line-height: 0.95; color: var(--orange); letter-spacing: -1px; }
  .lead-in { font-family: "Montserrat", sans-serif; font-weight: 700; font-size: 22px; color: var(--white); letter-spacing: 1.5px; margin-top: 26px; }
  .tagline { font-family: "Montserrat", sans-serif; font-weight: 800; font-size: 48px; line-height: 1.22; color: var(--white); letter-spacing: 2px; margin-top: 14px; }

  .benefits { position: absolute; top: 610px; left: 0; width: 896px; height: 325px; display: flex; padding: 30px 40px 0; }
  .benefit { flex: 1; display: flex; flex-direction: column; align-items: center; padding: 6px 16px 0; }
  .benefit + .benefit { border-left: 2px dashed var(--divider); }
  .benefit-icon { width: 116px; height: 116px; border-radius: 50%; background: var(--brand-blue); display: flex; align-items: center; justify-content: center; }
  .benefit-text { margin-top: 30px; font-size: 18px; line-height: 1.25; color: var(--ink); }
  .benefit-text.centered { text-align: center; margin-top: 48px; }
  .benefit-text.left { align-self: flex-start; }
  .highlight { color: var(--brand-blue); font-weight: 900; font-size: 26px; }

  .call-box { position: absolute; top: 962px; left: 48px; width: 356px; height: 160px; background: var(--orange); padding: 14px 20px; z-index: 2; }
  .call-title { font-family: "Montserrat", sans-serif; font-weight: 700; font-size: 35px; color: var(--white); letter-spacing: 1px; line-height: 1; }
  .call-sub { font-family: "Montserrat", sans-serif; font-weight: 400; font-size: 21px; color: var(--white); margin-top: 6px; }
  .call-line { display: flex; align-items: center; gap: 14px; color: var(--brand-blue); margin-top: 4px; }
  .call-phone { font-family: "Montserrat", sans-serif; font-weight: 800; font-size: 28px; }
  .call-web { font-family: "Montserrat", sans-serif; font-weight: 700; font-size: 21px; }
  .call-fold { position: absolute; top: 1122px; left: 48px; z-index: 1; }

  .agent { position: absolute; top: 1022px; left: 470px; }
  .agent-name, .agent-firm { font-family: "Montserrat", sans-serif; font-weight: 700; font-size: 17px; color: var(--orange); letter-spacing: 1px; line-height: 1.3; }
  .agent-lines { display: flex; gap: 44px; margin-top: 12px; font-size: 19px; font-weight: 700; color: var(--ink); }
  .agent-lines span { display: flex; align-items: center; gap: 10px; }

  .footer-bar { position: absolute; left: 0; bottom: 0; width: 896px; height: 78px; background: var(--footer-grey); display: flex; align-items: center; justify-content: flex-end; padding-right: 62px; gap: 10px; color: var(--white); font-family: "Montserrat", sans-serif; font-weight: 700; font-size: 14px; }
</style>
</head>
<body>
  <header class="masthead">
    <span class="brand-mark"></span>
    <span class="brand-name">Navelock Insurance Solutions</span>
  </header>

  <section class="hero">
    <div class="hero-photo" role="img" aria-label="Photo of a businessman holding a glowing dollar sign in cupped hands"></div>
    <div class="hero-copy">
      <h1 class="headline">READ<br>ONLY</h1>
      <p class="lead-in">IF YOU CARE ABOUT YOUR</p>
      <p class="tagline">BUSINESS'S<br>BOTTOM LINE</p>
    </div>
  </section>

  <section class="benefits">
    <div class="benefit">
      <div class="benefit-icon">
        <svg width="60" height="60" viewBox="0 0 60 60" fill="none" stroke="#fff" stroke-width="3">
          <circle cx="30" cy="30" r="24"/>
          <text x="30" y="41" text-anchor="middle" font-family="Lato, sans-serif" font-size="32" font-weight="900" fill="#fff" stroke="none">$</text>
        </svg>
      </div>
      <p class="benefit-text left">How would you like to pay<br><span class="highlight">18% less</span> on your next<br>Workers Compensation<br>Renewal, at NO COST to you?</p>
    </div>
    <div class="benefit">
      <div class="benefit-icon">
        <svg width="60" height="60" viewBox="0 0 60 60" fill="none" stroke="#fff" stroke-width="3">
          <circle cx="30" cy="20" r="11"/>
          <path d="M10 54 C10 40 18 34 30 34 C42 34 50 40 50 54 Z"/>
        </svg>
      </div>
      <p class="benefit-text centered">You <span class="highlight">DON'T</span> even need to<br>change your current Broker<br>or Insurance Company.</p>
    </div>
    <div class="benefit">
      <div class="benefit-icon">
        <svg width="60" height="60" viewBox="0 0 60 60" fill="#fff">
          <circle cx="30" cy="30" r="12"/>
          <g>
            <rect x="27" y="6" width="6" height="10"/><rect x="27" y="44" width="6" height="10"/>
            <rect x="6" y="27" width="10" height="6"/><rect x="44" y="27" width="10" height="6"/>
            <rect x="27" y="6" width="6" height="10" transform="rotate(45 30 30)"/><rect x="27" y="44" width="6" height="10" transform="rotate(45 30 30)"/>
            <rect x="6" y="27" width="10" height="6" transform="rotate(45 30 30)"/><rect x="44" y="27" width="10" height="6" transform="rotate(45 30 30)"/>
          </g>
          <circle cx="30" cy="30" r="5" fill="#0355a3"/>
        </svg>
      </div>
      <p class="benefit-text left">We are <span class="highlight">NOT</span> Brokers or<br>Agents. We are licensed<br>Workers Compensation<br>Cost Reduction Specialists.</p>
    </div>
  </section>

  <div class="call-box">
    <p class="call-title">CALL US TODAY</p>
    <p class="call-sub">FOR A 5 MINUTE OVERVIEW</p>
    <p class="call-line">
      <svg width="20" height="20" viewBox="0 0 24 24" fill="none" stroke="#0355a3" stroke-width="2.2"><circle cx="12" cy="12" r="10"/><path d="M8 7 l2 0 1 3 -1.5 1 a7 7 0 0 0 3.5 3.5 l1-1.5 3 1 0 2 a2 2 0 0 1 -2 1 A10 10 0 0 1 7 9 a2 2 0 0 1 1-2z" fill="#0355a3" stroke="none"/></svg>
      <span class="call-phone">555-310-4827</span>
    </p>
    <p class="call-line">
      <svg width="20" height="20" viewBox="0 0 24 24" fill="none" stroke="#0355a3" stroke-width="2"><circle cx="12" cy="12" r="10"/><ellipse cx="12" cy="12" rx="4" ry="10"/><line x1="2" y1="12" x2="22" y2="12"/></svg>
      <span class="call-web">www.navelock.net</span>
    </p>
  </div>
  <svg class="call-fold" width="80" height="40" viewBox="0 0 80 40"><path d="M0 0 H80 V22 L40 30 L32 40 L0 28 Z" fill="var(--orange-dark)"/></svg>

  <div class="agent">
    <p class="agent-name">MARLON VESTEBY</p>
    <p class="agent-firm">NAVELOCK INSURANCE SOLUTIONS</p>
    <div class="agent-lines">
      <span>
        <svg width="16" height="16" viewBox="0 0 24 24" fill="none" stroke="#3176b5" stroke-width="2.2"><circle cx="12" cy="12" r="10"/><path d="M8 7 l2 0 1 3 -1.5 1 a7 7 0 0 0 3.5 3.5 l1-1.5 3 1 0 2 a2 2 0 0 1 -2 1 A10 10 0 0 1 7 9 a2 2 0 0 1 1-2z" fill="#3176b5" stroke="none"/></svg>
        555-218-7750
      </span>
      <span>
        <svg width="16" height="16" viewBox="0 0 24 24" fill="#3176b5"><rect x="6" y="2" width="12" height="6"/><rect x="2" y="9" width="20" height="9" rx="2"/><rect x="6" y="15" width="12" height="7" fill="#fff" stroke="#3176b5" stroke-width="2"/></svg>
        555-606-0193
      </span>
    </div>
  </div>

  <footer class="footer-bar">
    <svg width="14" height="18" viewBox="0 0 14 18" fill="#fff"><path d="M7 0 a7 7 0 0 1 7 7 c0 5 -7 11 -7 11 S0 12 0 7 a7 7 0 0 1 7-7z"/><circle cx="7" cy="7" r="2.5" fill="#4b4b4d"/></svg>
    <span>4810 HARBOR CREST WAY LINDENFIELD CA 90417</span>
  </footer>
</body>
</html>
```